Back Pain

Need a flyer similar to the attached draft. This is to be handed out to prospective patients. Note that Sketch Hive has already designed the logo. If you need a copy please contact me

```html
<!DOCTYPE html>
<html lang="en">
<head>
<meta charset="UTF-8">
<title>Tech Neck Flyer</title>
<link href="https://fonts.googleapis.com/css2?family=Anton&family=Montserrat:wght@300;500;600;700;800&display=swap" rel="stylesheet">
<style>
:root{
  --blue-top:#0a64ad;
  --blue-deep:#0b2f63;
  --navy:#0f3a73;
  --green:#8cc63f;
  --white:#ffffff;
  --ink:#1e1e1e;
  --grey-light:#d9d9d9;
  --grey-dark:#6f6f6f;
  --skin:#e9c7b3;
  --pain:#f05a2a;
}
*{margin:0;padding:0;box-sizing:border-box}
html,body{width:800px;height:1200px;overflow:hidden;background:#fff}
body{font-family:'Montserrat',sans-serif;color:var(--white)}
.flyer{position:relative;width:800px;height:1200px;overflow:hidden}
.hero{position:absolute;left:0;top:0;width:800px;height:726px;background:linear-gradient(180deg,var(--blue-top) 0%,var(--blue-deep) 100%)}
.hero-photo{position:absolute;left:0;top:40px;width:440px;height:686px;background:radial-gradient(circle at 22% 28%,rgba(240,60,60,.7) 0,rgba(240,60,60,0) 16%),linear-gradient(120deg,var(--grey-light) 0%,#a9a9a9 55%,var(--grey-dark) 100%);clip-path:polygon(28% 0,62% 2%,78% 30%,92% 48%,100% 62%,72% 70%,50% 80%,40% 100%,0 100%,0 22%)}
.callouts{position:absolute;left:0;top:0}
.label{position:absolute;font-weight:600;font-size:16px;line-height:20px;letter-spacing:.5px;white-space:nowrap}
.brand{position:absolute;left:467px;top:100px;width:230px;text-align:center}
.brand-mark{display:block;width:56px;height:56px;border-radius:50%;background:var(--white);margin:-48px auto 10px}
.brand-name{font-weight:600;font-size:17px;line-height:1}
.brand-sub{font-weight:500;font-size:8px;letter-spacing:1.4px;margin-top:3px}
.title{position:absolute;left:462px;top:192px;font-family:'Anton',sans-serif;font-size:78px;line-height:1;letter-spacing:-1px}
.title .accent{color:var(--green)}
.lead{position:absolute;left:470px;top:306px;font-weight:300;font-size:20px;line-height:27px;letter-spacing:.3px}
.chart{position:absolute;left:0;top:0}
.chart-axis{position:absolute;left:742px;top:442px;transform:translate(-50%,-50%) rotate(-90deg);font-size:13px;font-weight:500;white-space:nowrap}
.stat{position:absolute;left:568px;top:633px;font-weight:700;font-size:12px;line-height:15px}
.stat .big{color:var(--green);font-size:17px;line-height:20px;letter-spacing:.4px}
.band{position:absolute;left:0;top:729px;width:800px;height:149px;background:var(--green);text-align:center;color:var(--navy)}
.band-l1{margin-top:30px;font-weight:800;font-size:25px;letter-spacing:.6px}
.band-l1 .dark{color:var(--ink)}
.band-l2{font-weight:800;font-size:25px;letter-spacing:.6px;color:var(--ink);margin-top:2px}
.band-l3{font-weight:600;font-size:16px;color:var(--navy);margin-top:2px}
.contact{position:absolute;left:0;top:878px;width:800px;height:322px;background:var(--white);color:var(--ink)}
.knee-photo{position:absolute;right:0;top:6px;width:210px;height:316px;background:radial-gradient(circle at 40% 52%,var(--pain) 0,rgba(240,90,42,.6) 18%,rgba(233,199,179,0) 34%),linear-gradient(100deg,#fff 0%,var(--skin) 35%,#d9a88e 100%);clip-path:polygon(12% 0,100% 0,100% 100%,40% 100%,28% 70%,6% 42%)}
.doctor{position:absolute;left:55px;top:28px;font-family:'Anton',sans-serif;font-size:48px;line-height:1;letter-spacing:-.5px}
.address{position:absolute;left:57px;top:92px;font-weight:600;font-size:21px;line-height:28px;letter-spacing:.4px}
.offer-pill{position:absolute;left:128px;top:181px;width:264px;height:50px;border-radius:0 16px 16px 0;background:var(--navy);color:var(--white);font-weight:700;font-size:16.5px;line-height:50px;padding-left:24px;letter-spacing:.3px;white-space:nowrap}
.offer-badge{position:absolute;left:47px;top:158px;width:88px;height:88px;border-radius:50%;background:var(--green);border:3px dotted var(--white);box-shadow:0 0 0 2px var(--green);text-align:center;line-height:84px;font-family:'Anton',sans-serif;font-size:34px;color:var(--white)}
.knee-icon{position:absolute;left:408px;top:108px;width:116px;height:116px;border-radius:50%;border:3px solid #f2a51a;background:linear-gradient(135deg,#fde4cf,#f7b98f)}
.book{position:absolute;left:57px;top:259px;font-weight:700;font-size:19px;letter-spacing:.3px}
.url{position:absolute;left:277px;top:255px;width:315px;height:31px;background:var(--green);clip-path:polygon(4% 0,100% 0,100% 100%,0 100%);color:var(--ink);font-weight:700;font-size:16px;line-height:31px;padding-left:22px}
</style>
</head>
<body>
<main class="flyer">
  <section class="hero">
    <div class="hero-photo" role="img" aria-label="Photo of a shirtless man holding his sore neck, shown in greyscale with red highlight at the neck"></div>

    <svg class="callouts" width="440" height="726" viewBox="0 0 440 726" aria-hidden="true">
      <g fill="none" stroke="#ffffff" stroke-width="1" stroke-dasharray="2 2" opacity=".8">
        <polyline points="87,205 87,41 366,41"/>
        <polyline points="297,123 370,123"/>
        <polyline points="244,287 244,281 331,281"/>
        <polyline points="220,338 220,532"/>
        <polyline points="24,603 220,603"/>
        <polyline points="105,666 220,666"/>
      </g>
      <g fill="#8cc63f" stroke="#ffffff" stroke-width="2">
        <circle cx="366" cy="41" r="5"/>
        <circle cx="297" cy="123" r="7"/>
        <circle cx="370" cy="123" r="5"/>
        <circle cx="87" cy="205" r="9"/>
        <circle cx="244" cy="287" r="8"/>
        <circle cx="331" cy="281" r="5"/>
        <circle cx="220" cy="338" r="8"/>
        <circle cx="220" cy="532" r="5"/>
        <circle cx="24" cy="603" r="8"/>
        <circle cx="220" cy="603" r="5"/>
        <circle cx="105" cy="666" r="8"/>
        <circle cx="220" cy="666" r="5"/>
      </g>
    </svg>
    <span class="label" style="left:329px;top:52px">NECK PAIN</span>
    <span class="label" style="left:334px;top:136px">HEADACHES</span>
    <span class="label" style="left:325px;top:302px">ARM PAIN</span>
    <span class="label" style="left:214px;top:546px">SHOULDER PAIN</span>
    <span class="label" style="left:213px;top:615px">BACK PAIN</span>
    <span class="label" style="left:214px;top:678px">SCIATICA</span>

    <div class="brand">
      <span class="brand-mark" aria-hidden="true"></span>
      <div class="brand-name">SPINE EASE CLINIC</div>
      <div class="brand-sub">DR SAM CARVER - CHIROPRACTOR</div>
    </div>

    <h1 class="title">TECH <span class="accent">NECK</span></h1>
    <p class="lead">As the head tilts forward.<br>More force is placed<br>on the spine</p>

    <svg class="chart" width="800" height="726" viewBox="0 0 800 726" aria-label="Bar chart of pressure on spine by head angle">
      <rect x="462" y="440" width="30" height="32" fill="#8cc63f" role="img" aria-label="Head profile icon"/>
      <g fill="#ffffff">
        <rect x="463" y="498" width="28" height="44"/>
        <rect x="528" y="467" width="28" height="75"/>
        <rect x="584" y="422" width="28" height="120"/>
        <rect x="634" y="386" width="28" height="156"/>
        <rect x="686" y="344" width="28" height="198"/>
      </g>
      <g font-family="Anton, sans-serif" font-size="20" fill="#1e1e1e" text-anchor="middle">
        <text x="477" y="528">12</text>
        <text x="542" y="495">27</text>
        <text x="598" y="450">40</text>
        <text x="648" y="414">49</text>
        <text x="700" y="372">60</text>
      </g>
      <g font-family="Montserrat, sans-serif" font-size="15" fill="#ffffff" text-anchor="middle">
        <text x="477" y="563">0°</text>
        <text x="542" y="563">15°</text>
        <text x="598" y="563">30°</text>
        <text x="648" y="563">45°</text>
        <text x="700" y="563">60°</text>
      </g>
      <circle cx="510" cy="644" r="47" fill="#ffffff"/>
      <path d="M510 644 L510 597 A47 47 0 0 1 527 688 Z" fill="#8cc63f"/>
    </svg>
    <span class="chart-axis">Pressure on spine (LBS)</span>

    <p class="stat">THE AVERAGE PERSON SPENDS<br><span class="big">8-11 HOURS PER DAY</span><br>USING ELECTRONIC DEVICES</p>
  </section>

  <section class="band">
    <p class="band-l1">CHIROPRACTIC CARE <span class="dark">CAN HELP</span></p>
    <p class="band-l2">CORRECT AND PREVENT THESE PROBLEMS</p>
    <p class="band-l3">By Restoring And Maintaining Proper Alignment Of The Neck</p>
  </section>

  <section class="contact">
    <div class="knee-photo" role="img" aria-label="Photo of hands holding a painful knee with orange glow"></div>
    <h2 class="doctor">DR SAMUEL CARVER</h2>
    <p class="address">Now in Northbay At<br>42 Harbour Rd - Studio Suites</p>
    <div class="offer-pill">Off Initial consultation</div>
    <div class="offer-badge">50%</div>
    <div class="knee-icon" role="img" aria-label="Illustration of a knee joint in a circle"></div>
    <p class="book">If now book on line at</p>
    <p class="url">www.spineeaseclinic.example</p>
  </section>
</main>
</body>
</html>
```